Holiday Rental Leaflet

Want a DL size double sided leaflet to distribute via local businesses, markets, family and friends
HOLIDAY RENTALCarrickalinga - 17 Farrow Street Sleeps 8-10 (2 Queen, 1 Double, 2 bunks), 4 bedrooms, BIR to all bedrooms 2 Bathrooms, one with bath, 2 toilets Open Plan Lounge/Dining/Kitchen area Dining Table for 8 peopleReverse cycle airconditionerSlow combustion wood heaterTV/DVD, CD/RadioKitchen has m/wave, oven, fridge/freezer, dishwasherBBQ providedTimber decking with 2 outside tables and 12 chairs Washing Machine and dryer provided One street back from beach Smoke free zone No Pets
For further information or to book contact Joan on 0491 278 306 or email joanbirch62@veltranet.com.au

Requirements
Nice to have
• Have sent a variety of photos of the house. No need to use all of them, pick out the most relevant for the leaflet.

```html
<!DOCTYPE html>
<html lang="en">
<head>
<meta charset="utf-8">
<title>Holiday Rental Leaflet – Carrickalinga</title>
<link rel="stylesheet" href="https://fonts.googleapis.com/css2?family=Open+Sans:wght@400;600;700;800&family=Baloo+2:wght@800&display=swap">
<style>
:root{
  --canvas:#e9ebef;
  --sky:#dff0fb;
  --sky-deep:#9fd3f1;
  --teal:#1fa3c9;
  --orange:#f39a1e;
  --orange-deep:#ea6b1f;
  --pink:#d81f57;
  --pink-deep:#b3164a;
  --green:#8cc63f;
  --green-deep:#5f9e2a;
  --wood:#8a5a2b;
  --wood-light:#b07a41;
  --sun:#f6d34a;
  --white:#ffffff;
  --ink:#ffffff;
}
*{box-sizing:border-box;margin:0;padding:0}
html,body{width:1200px;height:1000px;overflow:hidden}
body{background:var(--canvas);font-family:"Open Sans",Arial,sans-serif;position:relative}
.page{position:absolute;top:110px;width:540px;height:780px;overflow:hidden;
  background:linear-gradient(160deg,var(--white) 0%,var(--sky) 45%,var(--sky-deep) 100%);
  box-shadow:0 6px 24px rgba(0,0,0,.18)}
.page--front{left:40px}
.page--back{left:620px}
.page svg.decor{position:absolute;inset:0;width:540px;height:780px}
.photo{position:absolute;border-radius:50%;overflow:hidden}
.photo--ring-purple{border:6px solid #8e6fc4}
.photo--ring-blue{border:6px solid #5cc3e8}
.photo--ring-yellow{border:6px solid #e6e23a}
.photo--ring-green{border:6px solid var(--green)}
.photo--ring-white{border:6px solid var(--white)}
.sign{position:absolute;left:220px;top:50px;width:300px;height:210px;transform:rotate(6deg)}
.sign__board{position:absolute;inset:0;border-radius:10px;
  background:linear-gradient(180deg,var(--wood-light),var(--wood));box-shadow:0 6px 12px rgba(0,0,0,.3)}
.sign__title{position:absolute;inset:0;display:flex;flex-direction:column;align-items:center;justify-content:center;
  font-family:"Baloo 2",Arial,sans-serif;font-weight:800;font-size:58px;line-height:.95;color:var(--sun)}
.address{position:absolute;left:28px;top:470px;width:300px;height:110px;border-radius:14px;
  background:var(--pink);color:var(--ink);font-size:25px;line-height:1.25;font-weight:400;
  display:flex;flex-direction:column;justify-content:center;padding-left:36px;letter-spacing:.5px;
  transform:rotate(-3deg)}
.contact{position:absolute;color:var(--ink)}
.contact__lead{font-size:17px;font-weight:400;line-height:1.25;text-transform:uppercase}
.contact__main{font-size:31px;font-weight:800;text-transform:uppercase;white-space:nowrap}
.page--front .contact{right:18px;bottom:22px;text-align:right;transform:rotate(-4deg)}
.page--back .contact{right:16px;bottom:16px;text-align:right;transform:rotate(2deg)}
.page--back .contact__main{font-size:28px}
.phone-tag{position:absolute}
.features{position:absolute;top:430px;height:240px;border-radius:12px;
  background:linear-gradient(180deg,var(--pink),var(--pink-deep));color:var(--ink);
  list-style:none;padding:10px 10px 10px 12px;font-size:13.2px;line-height:1.3}
.features li{position:relative;padding-left:20px;margin-bottom:1px}
.features li::before{content:"";position:absolute;left:3px;top:5px;width:7px;height:7px;border-radius:50%;
  background:var(--white);box-shadow:0 0 0 2px var(--pink),0 0 0 3px rgba(255,255,255,.8)}
.features--left{left:14px;width:232px}
.features--right{left:258px;width:270px;font-size:14.4px}
</style>
</head>
<body>

<section class="page page--front" aria-label="Leaflet front">
  <svg class="decor" viewBox="0 0 540 780" aria-hidden="true">
    <defs>
      <linearGradient id="houseFront" x1="0" y1="0" x2="0" y2="1">
        <stop offset="0" stop-color="#c9d3d8"/><stop offset=".5" stop-color="#6d7470"/><stop offset="1" stop-color="#7ea64a"/>
      </linearGradient>
    </defs>
    <path d="M0 60 Q220 30 430 70 L430 560 Q200 600 0 520 Z" fill="url(#houseFront)"/>
    <path d="M0 80 Q250 -10 520 60" fill="none" stroke="var(--orange-deep)" stroke-width="5"/>
    <path d="M0 570 Q260 640 540 470" fill="none" stroke="var(--orange)" stroke-width="14"/>
    <path d="M0 640 Q270 690 540 560 L540 600 Q280 720 0 690 Z" fill="var(--teal)"/>
    <path d="M0 690 Q280 720 540 600 L540 780 L0 780 Z" fill="var(--green)"/>
  </svg>
  <div role="img" aria-label="Photo of the holiday house with carport and lawn" style="position:absolute;left:0;top:60px;width:430px;height:480px"></div>

  <div class="sign">
    <div class="sign__board" role="img" aria-label="Wooden hanging sign"></div>
    <h1 class="sign__title"><span>Holiday</span><span>Rental</span></h1>
  </div>

  <div class="photo photo--ring-purple" role="img" aria-label="Photo of the slow combustion wood heater"
       style="left:395px;top:330px;width:140px;height:140px;background:radial-gradient(circle at 50% 60%,#6b3a2a,#b07b5a 70%,#d9c3a8)"></div>
  <div class="photo photo--ring-blue" role="img" aria-label="Photo of the timber dining area"
       style="left:332px;top:480px;width:128px;height:128px;background:radial-gradient(circle at 50% 60%,#c98b4a,#e6b77d 70%,#f0dcc0)"></div>

  <div class="address"><span>CARRICKALINGA</span><span>17 FARROW STREET</span></div>

  <svg class="phone-tag" style="left:30px;top:670px" width="44" height="52" viewBox="0 0 44 52" aria-hidden="true">
    <path d="M0 0 H44 V40 H16 L6 52 V40 H0 Z" fill="var(--pink)"/>
    <path d="M14 10 q-4 4 2 14 q6 9 14 6 l-3 -5 q-3 2 -6 -2 q-4 -5 -1 -8 Z" fill="var(--white)"/>
  </svg>

  <div class="contact">
    <p class="contact__lead">For further<br>information or to book</p>
    <p class="contact__main">Contact Joan on: 0491 278 306</p>
  </div>
</section>

<section class="page page--back" aria-label="Leaflet back">
  <svg class="decor" viewBox="0 0 540 780" aria-hidden="true">
    <defs>
      <linearGradient id="houseBack" x1="0" y1="0" x2="0" y2="1">
        <stop offset="0" stop-color="#cfe3c4"/><stop offset=".45" stop-color="#6c7072"/><stop offset="1" stop-color="#a89a7c"/>
      </linearGradient>
    </defs>
    <circle cx="270" cy="170" r="285" fill="url(#houseBack)"/>
    <circle cx="270" cy="170" r="285" fill="none" stroke="var(--orange)" stroke-width="14"/>
    <path d="M440 -10 Q560 120 500 260" fill="none" stroke="var(--orange)" stroke-width="14"/>
    <path d="M0 676 L540 706 L540 780 L0 780 Z" fill="var(--green)"/>
    <path d="M0 668 L540 698 L540 708 L0 678 Z" fill="var(--green-deep)"/>
  </svg>
  <div role="img" aria-label="Photo of the house with timber deck and umbrellas" style="position:absolute;left:0;top:0;width:540px;height:430px"></div>

  <div class="photo photo--ring-white" role="img" aria-label="Photo of the sea view"
       style="left:380px;top:55px;width:170px;height:170px;background:linear-gradient(180deg,#8cc6e6 0%,#2f6fa6 40%,#1d4f80 70%,#3f6b3a 100%)"></div>
  <div class="photo photo--ring-yellow" role="img" aria-label="Photo of the beach"
       style="left:30px;top:335px;width:140px;height:140px;background:linear-gradient(180deg,#bfe0f2 0%,#6fb2cf 40%,#e7dcc3 70%,#b9a079 100%)"></div>
  <div class="photo photo--ring-green" role="img" aria-label="Photo of a queen bedroom"
       style="left:250px;top:310px;width:185px;height:185px;background:radial-gradient(circle at 50% 70%,#d9a0a4,#a8683a 60%,#7a4a26)"></div>

  <ul class="features features--left">
    <li>4 bedrooms - Sleeps 8 -10 (2 Queen, 1 Double, 2 bunks)</li>
    <li>BIR to all bedrooms</li>
    <li>2 Bathrooms, 1 with bath, 2 toilets</li>
    <li>Open Plan Lounge/Dining/ Kitchen area</li>
    <li>Dining Table for 8 people</li>
    <li>Reverse cycle airconditioner</li>
    <li>Slow combustion wood heater</li>
    <li>TV/DVD, CD/Radio</li>
  </ul>
  <ul class="features features--right">
    <li>Kitchen has: microwave, oven, fridge/freezer, dishwasher</li>
    <li>BBQ provided</li>
    <li>Timber decking with 2 outside tables and 12 chairs</li>
    <li>Washing Machine and dryer provided</li>
    <li>One street back from beach</li>
    <li>Smoke free zone</li>
    <li>No Pets</li>
  </ul>

  <svg class="phone-tag" style="left:4px;top:674px" width="56" height="52" viewBox="0 0 56 52" aria-hidden="true">
    <path d="M0 0 H38 L56 26 L38 52 H0 Z" fill="var(--green-deep)"/>
    <circle cx="24" cy="26" r="17" fill="var(--white)"/>
    <path d="M17 17 q-4 4 2 13 q6 8 13 5 l-3 -5 q-3 2 -5 -2 q-4 -4 -1 -7 Z" fill="var(--green-deep)"/>
  </svg>

  <div class="contact">
    <p class="contact__lead">For further information or to book</p>
    <p class="contact__main">Contact Joan on: 0491 278 306</p>
  </div>
</section>

</body>
</html>
```